Business Card Design Project

We need a business card to reflect the design of our website - just so it all ties in - it has a retro feel and can be found at http://www.velorasoulpair.com
We will need our phone 0437 215 964
Web address, and email velorapair@fernmail.com included
Our catch cry is "Classic Cocktail Music"
Perfect Live Music for Private & Corporate Events, Weddings and Dinner Music
Our names should be included :-
Maribel Thorne / piano & Dennis Holloway / bass
I am now also including our logo so that it can be included (in part or whole) somehow in the design
My partner thinks we should include our logo in some form in the design of the card - i will attach this here for you. I will attach eps but if you prefer another format please let me know
Regards
Mari

```html
<!DOCTYPE html>
<html lang="en">
<head>
<meta charset="utf-8">
<title>Velora Pair – Business Card</title>
<link href="https://fonts.googleapis.com/css2?family=Federo&family=Anton&family=Cabin:wght@500;600&family=Josefin+Sans:wght@400;600&display=swap" rel="stylesheet">
<style>
  :root {
    --bg: #e9e6df;
    --teal: #6aa9ad;
    --teal-dark: #568f93;
    --teal-text: #74b3b7;
    --cream: #d8d4c6;
    --cream-light: #e2ded2;
    --red: #c8472c;
    --red-dark: #a9391f;
    --ink: #1c1c1c;
    --charcoal: #3a3a3c;
    --ribbon: #ece5cf;
    --ribbon-shade: #c9bf9f;
    --white: #ffffff;
    --dot: #b8b3a4;
    --faint: #bdb9ad;
  }
  * { box-sizing: border-box; margin: 0; padding: 0; }
  html, body { width: 1200px; height: 800px; overflow: hidden; }
  body {
    background: var(--bg);
    display: flex;
    align-items: center;
    justify-content: center;
    gap: 40px;
    font-family: "Josefin Sans", sans-serif;
  }
  .card {
    position: relative;
    width: 560px;
    height: 320px;
    background: var(--cream);
    overflow: hidden;
    box-shadow: 0 10px 24px rgba(0,0,0,.18);
  }
  .card-shapes { position: absolute; inset: 0; }
  .brand-name {
    position: absolute;
    left: 0; right: 0;
    text-align: center;
    font-family: "Federo", sans-serif;
    color: var(--teal-text);
    letter-spacing: 2px;
    text-transform: uppercase;
  }
  .tagline {
    position: absolute;
    font-family: "Anton", sans-serif;
    color: var(--ink);
    letter-spacing: 1.5px;
    text-transform: uppercase;
    text-align: center;
  }
  .website {
    position: absolute;
    left: 0; right: 0;
    text-align: center;
    font-family: "Josefin Sans", sans-serif;
    font-size: 13px;
    letter-spacing: 1.5px;
    color: var(--charcoal);
  }
  /* front */
  .card-front .brand-name { top: 150px; font-size: 30px; }
  .card-front .tagline { top: 186px; left: 150px; width: 260px; font-size: 20px; line-height: 28px; }
  .card-front .website { top: 226px; }
  .social-band {
    position: absolute;
    left: 0; right: 0; bottom: 0;
    height: 66px;
    display: flex;
    align-items: center;
    justify-content: space-between;
    padding: 0 26px;
    color: var(--white);
    font-family: "Cabin", sans-serif;
    font-weight: 600;
    font-size: 15px;
  }
  .social-link { display: flex; align-items: center; gap: 10px; }
  .social-mark { width: 22px; height: 22px; background: var(--white); border-radius: 4px; }
  .social-mark.round { border-radius: 50%; }
  .social-divider { font-weight: 500; opacity: .85; }
  /* back */
  .card-back .brand-name { left: 200px; right: 0; top: 108px; font-size: 24px; }
  .card-back .tagline { top: 138px; left: 282px; width: 220px; font-size: 16px; line-height: 22px; }
  .contact-list {
    position: absolute;
    left: 250px; top: 180px;
    list-style: none;
    display: flex;
    flex-direction: column;
    gap: 8px;
    font-family: "Cabin", sans-serif;
    font-weight: 500;
    font-size: 13px;
    color: var(--charcoal);
  }
  .contact-item { display: flex; align-items: center; gap: 12px; }
  .contact-icon { width: 20px; height: 20px; flex: none; }
</style>
</head>
<body>

<!-- Back of card: contact details -->
<section class="card card-back" aria-label="Card back">
  <svg class="card-shapes" width="560" height="320" viewBox="0 0 560 320" aria-hidden="true">
    <rect x="0" y="0" width="560" height="70" fill="var(--teal)"/>
    <circle cx="340" cy="66" r="42" fill="var(--teal)"/>
    <circle cx="340" cy="66" r="32" fill="var(--charcoal)" stroke="var(--teal-dark)" stroke-width="2"/>
    <rect x="0" y="302" width="560" height="18" fill="var(--red)"/>
    <circle cx="120" cy="180" r="88" fill="var(--faint)" opacity=".55"/>
    <line x1="200" y1="170" x2="270" y2="170" stroke="var(--dot)" stroke-width="1.5" stroke-dasharray="2 4"/>
    <polygon points="268,140 282,140 282,160 268,160 274,150" fill="var(--ribbon-shade)"/>
    <polygon points="502,140 516,140 510,150 516,160 502,160" fill="var(--ribbon-shade)"/>
    <rect x="280" y="136" width="224" height="26" fill="var(--ribbon)"/>
  </svg>
  <div class="brand-name">Velora Pair</div>
  <div class="tagline">Classic Cocktail Music</div>
  <ul class="contact-list">
    <li class="contact-item">
      <svg class="contact-icon" viewBox="0 0 20 20" aria-hidden="true"><circle cx="10" cy="10" r="10" fill="var(--red)"/><circle cx="10" cy="8" r="3" fill="var(--white)"/><path d="M5 15 a5 4 0 0 1 10 0z" fill="var(--white)"/></svg>
      <span>Maribel Thorne / piano &amp; Dennis Holloway / bass</span>
    </li>
    <li class="contact-item">
      <svg class="contact-icon" viewBox="0 0 20 20" aria-hidden="true"><circle cx="10" cy="10" r="10" fill="var(--red)"/><path d="M6.5 5.5 l2 0 l1 2.5 l-1.3 1 a6 6 0 0 0 2.8 2.8 l1-1.3 l2.5 1 l0 2 a1.5 1.5 0 0 1-1.5 1 a8 8 0 0 1-7.5-7.5 a1.5 1.5 0 0 1 1-1.5z" fill="var(--white)"/></svg>
      <span>0437 215 964</span>
    </li>
    <li class="contact-item">
      <svg class="contact-icon" viewBox="0 0 20 20" aria-hidden="true"><circle cx="10" cy="10" r="10" fill="var(--red)"/><rect x="5" y="6.5" width="10" height="7" fill="var(--white)"/><polyline points="5,6.5 10,10.5 15,6.5" fill="none" stroke="var(--red)" stroke-width="1"/></svg>
      <span>velorapair@fernmail.com</span>
    </li>
    <li class="contact-item">
      <svg class="contact-icon" viewBox="0 0 20 20" aria-hidden="true"><circle cx="10" cy="10" r="10" fill="var(--red)"/><circle cx="10" cy="10" r="5" fill="none" stroke="var(--white)" stroke-width="1.3"/><ellipse cx="10" cy="10" rx="2.2" ry="5" fill="none" stroke="var(--white)" stroke-width="1.1"/><line x1="5" y1="10" x2="15" y2="10" stroke="var(--white)" stroke-width="1.1"/></svg>
      <span>http://www.velorasoulpair.com</span>
    </li>
  </ul>
</section>

<!-- Front of card: name, tagline, social -->
<section class="card card-front" aria-label="Card front">
  <svg class="card-shapes" width="560" height="320" viewBox="0 0 560 320" aria-hidden="true">
    <defs>
      <pattern id="band-stripes" width="56" height="100" patternUnits="userSpaceOnUse">
        <rect width="56" height="100" fill="var(--teal)"/>
        <line x1="0.5" y1="0" x2="0.5" y2="100" stroke="var(--teal-dark)" stroke-width="1" opacity=".45"/>
      </pattern>
    </defs>
    <rect x="0" y="0" width="560" height="100" fill="url(#band-stripes)"/>
    <circle cx="280" cy="92" r="52" fill="var(--teal)"/>
    <path d="M0 92 H230 A50 50 0 0 0 330 92 H560" fill="none" stroke="var(--teal-dark)" stroke-width="1.2" stroke-dasharray="5 3"/>
    <circle cx="280" cy="92" r="40" fill="var(--charcoal)" stroke="var(--teal-dark)" stroke-width="2"/>
    <line x1="24" y1="168" x2="150" y2="168" stroke="var(--dot)" stroke-width="2" stroke-dasharray="2 8"/>
    <line x1="410" y1="218" x2="536" y2="218" stroke="var(--dot)" stroke-width="2" stroke-dasharray="2 8"/>
    <polygon points="132,186 152,186 152,214 132,214 140,200" fill="var(--ribbon-shade)"/>
    <polygon points="408,186 428,186 420,200 428,214 408,214" fill="var(--ribbon-shade)"/>
    <rect x="148" y="182" width="264" height="32" fill="var(--ribbon)"/>
    <rect x="0" y="254" width="560" height="66" fill="var(--red)"/>
    <rect x="0" y="314" width="560" height="6" fill="var(--red-dark)"/>
  </svg>
  <div class="brand-name">Velora Pair</div>
  <div class="tagline">Classic Cocktail Music</div>
  <div class="website">WWW.VELORASOULPAIR.COM</div>
  <div class="social-band">
    <span class="social-link"><span class="social-mark"></span>Chatterbook.com/velorapair</span>
    <span class="social-divider">/</span>
    <span class="social-link"><span class="social-mark round"></span>Chirpline.com/velorapair</span>
  </div>
</section>

</body>
</html>
```